Corinne Dabney Interiors business cards

We need a DOUBLE SIDED business card design that is simple, elegant and modern. We are a rapidly growing Interior Design Firm, and our brand colours are blush pink, navy, and antique gold, so we require some or all of these colours to be used. The final design should portray elegance, simplicity, and have a modern feel. We have upload inspiration photos that have the feel we're looking for.

Industry/Entity Type

Interior Design

Contact Information for Business Card

Contact information and LOGO

Colors
EB3D1F
EC4F4E
F09395
F8D3D4
FCEDEE

Requirements
Must have
• Navy, the right shade of blush pink, and antique gold

```html
<!DOCTYPE html>
<html lang="en">
<head>
<meta charset="utf-8">
<title>Corinne Dabney Interiors — Business Cards</title>
<link rel="stylesheet" href="https://fonts.googleapis.com/css2?family=Montserrat:wght@400;500&family=Oswald:wght@300;500&display=swap">
<style>
  :root {
    --backdrop: #8ee3fc;
    --card: #ffffff;
    --blush: #f9dfe1;
    --blush-deep: #f4a7aa;
    --rose-gold: #e4b3a4;
    --rose-light: #f1cfc8;
    --coral: #ec5a55;
    --navy: #1b2758;
    --antique-gold: #8f7434;
    --gold-bright: #f9c76a;
    --gold-pale: #fff6dc;
  }
  * { margin: 0; padding: 0; box-sizing: border-box; }
  html, body {
    width: 1200px; height: 1200px; overflow: hidden;
    background: var(--backdrop);
  }
  .sheet { position: relative; width: 1200px; height: 1200px; }
  .card {
    position: absolute; left: 174px; width: 852px; height: 486px;
    background: var(--card); overflow: hidden;
    box-shadow: 0 6px 22px rgba(40, 110, 140, 0.25);
  }
  .card--front { top: 69px; }
  .card--back { top: 599px; }
  .card__art { position: absolute; inset: 0; width: 100%; height: 100%; display: block; }

  .person__name {
    position: absolute; left: 54px; top: 66px;
    font-family: "Oswald", sans-serif; font-weight: 300;
    font-size: 68px; line-height: 1; letter-spacing: 1px;
    color: var(--coral);
  }
  .person__title {
    position: absolute; left: 57px; top: 139px;
    font-family: "Oswald", sans-serif; font-weight: 500;
    font-size: 24px; line-height: 1; letter-spacing: 0.5px;
    color: var(--navy);
  }
  .contact { position: absolute; left: 56px; list-style: none; }
  .contact--direct { top: 250px; }
  .contact--online { top: 331px; }
  .contact__item {
    display: flex; align-items: center; height: 26px;
    font-family: "Montserrat", sans-serif; font-weight: 400;
    font-size: 20.5px; color: var(--coral);
  }
  .contact__icon { width: 14px; height: 14px; margin-right: 16px; flex: none; }
  .contact__mark { width: 12px; height: 12px; margin: 0 17px 0 1px; background: var(--navy); flex: none; }
  .contact__mark--round { border-radius: 50%; }

  .brand-name {
    position: absolute;
    font-family: "Montserrat", sans-serif; font-weight: 500;
    color: var(--antique-gold); text-transform: uppercase;
    text-align: center; line-height: 1.15;
  }
  .brand-name--front { left: 600px; width: 230px; top: 370px; font-size: 15px; letter-spacing: 0.5px; }
  .brand-name--back { left: 470px; width: 320px; top: 200px; font-size: 30px; letter-spacing: 1px; }
</style>
</head>
<body>
<main class="sheet">

  <section class="card card--front" aria-label="Card front">
    <svg class="card__art" viewBox="0 0 1372 782" preserveAspectRatio="none" aria-hidden="false">
      <defs>
        <linearGradient id="goldStripeA" x1="0" y1="0" x2="1" y2="1">
          <stop offset="0" stop-color="var(--gold-bright)"/>
          <stop offset="1" stop-color="var(--gold-pale)"/>
        </linearGradient>
        <linearGradient id="goldStripeB" x1="0" y1="1" x2="1" y2="0">
          <stop offset="0" stop-color="var(--gold-bright)"/>
          <stop offset="0.45" stop-color="var(--gold-pale)"/>
          <stop offset="1" stop-color="var(--gold-bright)"/>
        </linearGradient>
        <linearGradient id="roseFacets" x1="0" y1="0" x2="1" y2="1">
          <stop offset="0" stop-color="var(--rose-light)"/>
          <stop offset="0.5" stop-color="var(--rose-gold)"/>
          <stop offset="1" stop-color="var(--rose-light)"/>
        </linearGradient>
      </defs>
      <polygon points="725,0 1372,0 1372,22 1025,395" fill="url(#roseFacets)" role="img" aria-label="Rose gold and blush marble geometric pattern"/>
      <polygon points="705,782 1372,782 1372,30 1020,400" fill="var(--blush)"/>
      <line x1="685" y1="0" x2="1030" y2="395" stroke="url(#goldStripeA)" stroke-width="14"/>
      <line x1="690" y1="782" x2="1355" y2="0" stroke="url(#goldStripeB)" stroke-width="14"/>
    </svg>

    <h1 class="person__name">CORINNE DABNEY</h1>
    <p class="person__title">PRINCIPAL DESIGNER</p>

    <ul class="contact contact--direct">
      <li class="contact__item">
        <svg class="contact__icon" viewBox="0 0 16 16" aria-hidden="true"><path d="M4 1 L6.5 4.5 L5 6.2 C6 8.5 7.5 10 9.8 11 L11.5 9.5 L15 12 L13.3 15 C7 14.5 1.5 9 1 2.7 Z" fill="var(--navy)"/></svg>
        905-555-0142
      </li>
      <li class="contact__item">
        <svg class="contact__icon" viewBox="0 0 16 16" aria-hidden="true"><rect x="1" y="3.5" width="14" height="9.5" fill="var(--navy)"/><polyline points="1.5,4 8,9 14.5,4" fill="none" stroke="#fff" stroke-width="1.4"/></svg>
        corinne@cdinteriorsinc.com
      </li>
    </ul>

    <ul class="contact contact--online">
      <li class="contact__item">
        <svg class="contact__icon" viewBox="0 0 16 16" aria-hidden="true"><g fill="none" stroke="var(--navy)" stroke-width="1.5"><circle cx="8" cy="8" r="6.5"/><ellipse cx="8" cy="8" rx="2.8" ry="6.5"/><line x1="1.5" y1="8" x2="14.5" y2="8"/></g></svg>
        www.corinnedabneyinteriors.com
      </li>
      <li class="contact__item"><span class="contact__mark" aria-hidden="true"></span>corinnedabneyinteriors</li>
      <li class="contact__item"><span class="contact__mark contact__mark--round" aria-hidden="true"></span>corinne.dabney.interiors</li>
    </ul>

    <p class="brand-name brand-name--front">Corinne Dabney Interiors</p>
  </section>

  <section class="card card--back" aria-label="Card back">
    <svg class="card__art" viewBox="0 0 1372 782" preserveAspectRatio="none">
      <defs>
        <linearGradient id="goldStripeC" x1="0" y1="0" x2="1" y2="1">
          <stop offset="0" stop-color="var(--gold-bright)"/>
          <stop offset="0.5" stop-color="var(--gold-pale)"/>
          <stop offset="1" stop-color="var(--gold-bright)"/>
        </linearGradient>
        <linearGradient id="goldStripeD" x1="1" y1="0" x2="0" y2="1">
          <stop offset="0" stop-color="var(--gold-bright)"/>
          <stop offset="1" stop-color="var(--gold-pale)"/>
        </linearGradient>
        <linearGradient id="roseFacetsBack" x1="0" y1="0" x2="1" y2="1">
          <stop offset="0" stop-color="var(--rose-gold)"/>
          <stop offset="0.5" stop-color="var(--rose-light)"/>
          <stop offset="1" stop-color="var(--rose-gold)"/>
        </linearGradient>
      </defs>
      <polygon points="0,0 172,0 835,782 0,782" fill="url(#roseFacetsBack)" role="img" aria-label="Rose gold and blush marble geometric pattern"/>
      <polygon points="182,0 728,0 462,308" fill="var(--blush-deep)"/>
      <line x1="190" y1="0" x2="852" y2="782" stroke="url(#goldStripeC)" stroke-width="14"/>
      <line x1="745" y1="0" x2="445" y2="345" stroke="url(#goldStripeD)" stroke-width="14"/>
    </svg>

    <p class="brand-name brand-name--back">Corinne Dabney<br>Interiors</p>
  </section>

</main>
</body>
</html>
```